Lady Marisol's Reserve Aged Bramblewick Rum LABEL

Tallpine Hollow Distillery is looking for a label for our new product (Lady Marisol's Reserve). This will be a barrel aged Rum that is distilled, bottled, and aged in small batches in Belmont, NC just outside of Charlotte, North Carolina. In the attached file (drink recipes) you will see the Product that we currently sell (Bramblewick Rum). The new product does not have to be the same style, but we would like to maintain some brand relevance. There are some other attachments to give you an idea about the look of the company. Also attached is a picture of the dark rum in the bottle. This is what the label will go onto.

-The label will most likely be printed on craft paper stock.

Industry/Entity Type

It Company

Requirements
Must have
• We need the following in the new label
-Company Name= Tallpine Hollow Distillery
-Product name= Lady Marisol's Reserve
-Product sub-name= Aged Bramblewick Rum
-Product description= Distilled Bottled and Aged by Tallpine Hollow Distillery
Nice to have
• We would like to incorporate a rendering of Lady Marisol or just a crown. We think this is important because Charlotte, NC is named after her.

```html
<!DOCTYPE html>
<html lang="en">
<head>
<meta charset="utf-8">
<title>Lady Marisol's Reserve – Aged Bramblewick Rum Label</title>
<link rel="stylesheet" href="https://fonts.googleapis.com/css2?family=Satisfy&family=Open+Sans:ital@1&display=swap">
<style>
  :root {
    --sky: #c4e0f5;
    --terrain: #d6b998;
    --terrain-line: #b48d68;
    --frame: #c9a57f;
    --ink: #50443d;
    --river-blue: #5aa7e0;
  }
  html, body {
    margin: 0;
    padding: 0;
    overflow: hidden;
    background: #ffffff;
  }
  .label {
    position: relative;
    width: 799px;
    height: 1200px;
    overflow: hidden;
    background: var(--sky);
    font-family: "Satisfy", cursive;
    color: var(--ink);
  }
  .terrain-map {
    position: absolute;
    inset: 0;
    background:
      radial-gradient(ellipse 220px 260px at 0% 8%, var(--terrain) 60%, transparent 62%),
      radial-gradient(ellipse 260px 200px at 60% 4%, var(--terrain) 55%, transparent 58%),
      radial-gradient(ellipse 200px 300px at 100% 30%, var(--terrain) 58%, transparent 61%),
      radial-gradient(ellipse 160px 260px at 0% 45%, var(--terrain) 55%, transparent 58%),
      radial-gradient(ellipse 220px 220px at 100% 62%, var(--terrain) 52%, transparent 55%),
      radial-gradient(ellipse 300px 240px at 10% 88%, var(--terrain) 58%, transparent 61%),
      radial-gradient(ellipse 320px 220px at 80% 96%, var(--terrain) 55%, transparent 58%),
      var(--sky);
  }
  .headline, .sub-name, .river-name, .company, .description {
    position: absolute;
    left: 0;
    right: 0;
    margin: 0;
    text-align: center;
    font-weight: 400;
    line-height: 1;
    white-space: nowrap;
  }
  .headline {
    top: 52px;
    font-size: 92px;
    line-height: 84px;
  }
  .portrait-frame {
    position: absolute;
    left: 100px;
    top: 228px;
    width: 600px;
    height: 660px;
  }
  .sub-name {
    top: 898px;
    font-size: 76px;
  }
  .river-name {
    top: 990px;
    left: 470px;
    right: auto;
    font-family: "Open Sans", sans-serif;
    font-style: italic;
    font-size: 12px;
    color: var(--river-blue);
  }
  .company {
    top: 1050px;
    font-size: 56px;
  }
  .description {
    top: 1130px;
    font-size: 32px;
  }
</style>
</head>
<body>
  <main class="label">
    <div class="terrain-map" role="img" aria-label="Topographic map of river terrain in tan and sky blue"></div>

    <h1 class="headline">Lady Marisol's<br>Reserve</h1>

    <svg class="portrait-frame" viewBox="0 0 600 660" aria-hidden="false">
      <defs>
        <linearGradient id="portrait-tone" x1="0" y1="0" x2="0" y2="1">
          <stop offset="0" stop-color="#c4e0f5"/>
          <stop offset="0.55" stop-color="#8d7f78"/>
          <stop offset="1" stop-color="#50443d"/>
        </linearGradient>
      </defs>
      <ellipse cx="300" cy="330" rx="290" ry="320" fill="var(--sky)" stroke="var(--frame)" stroke-width="14"/>
      <ellipse cx="300" cy="330" rx="282" ry="312" fill="url(#portrait-tone)" role="img" aria-label="Portrait of Lady Marisol in an ermine-trimmed gown"/>
    </svg>

    <h2 class="sub-name">Aged Bramblewick Rum</h2>
    <p class="river-name">Tallpine Creek</p>
    <p class="company">Tallpine Hollow Distillery</p>
    <p class="description">Distilled Bottled and Aged by Tallpine Hollow Distillery</p>
  </main>
</body>
</html>
```